" Trabalhamos com Consultoria focada em Gestão Financeira. Nosso portfólio: * Raio-X Financeiro e Administrativo; É uma leitura técnica dos números para demonstrar ao cliente o desempenho das Receitas e Despesas da Empresa, bem como apontar a tendência para o próximo período, alertando sobre os riscos da operação. O resultado do Raio-x indicará o diagnóstico e possíveis soluções para equilibrar a saúde financeira da organização. *Estruturação das Rotinas de Gestão Financeira e Administrativa; Trata-se do Mapeamento e Redesenho dos processos e rotinas da área Financeira, tais como Contas a Receber, Contas a Pagar, Prestação de Contas, Interface com a Contabilidade, entre outras; *Transferência de Conhecimento; Neste bloco oferecemos uma capacitação (hands on) à equipe do Financeiro, sobre os temas mais importantes para uma boa Gestão Financeira. *Pré-Diagnóstico da Situação Fiscal, Contábil e Tributária; O cliente pode contratar também um pacote para realizarmos um pré-diagnóstico da situação Fiscal da empresa, avaliando a conformidade dos dados e procedimentos contábeis, e avaliando também se o regime tributário adotado é o que oferece o melhor custo benefício para a organização. *Monitoramento de Desempenho; Neste bloco o objetivo é identificar os indicadores de desempenho econômicos e financeiros, e traduzi-los de forma didática e intuitiva para o cliente acompanhar e fazer uma boa gestão no dia a dia. As informações são divulgadas através do Dashboard online desenvolvido pela Lumiara, com acesso via computadores e dispositivos móveis. *Operação Assistida; Após a execução dos serviços e produtos estruturantes, oferecemos ao cliente um acompanhamento periódico e sistemático das novas rotinas implantadas. "

```html
<!DOCTYPE html>
<html lang="pt-BR">
<head>
<meta charset="UTF-8">
<title>Lumiara — Cartão de Visita</title>
<link href="https://fonts.googleapis.com/css2?family=Montserrat:wght@400;500;600;700&display=swap" rel="stylesheet">
<style>
  :root {
    --navy: #1b2a52;
    --navy-deep: #15213f;
    --gold: #b8873f;
    --gold-light: #e0b673;
    --gold-dark: #7a5522;
    --white: #ffffff;
    --backdrop: #e9eaec;
    --ink: #1b2a52;
  }
  html, body {
    margin: 0;
    padding: 0;
    width: 1200px;
    height: 1200px;
    overflow: hidden;
    background: var(--backdrop);
    font-family: "Montserrat", Arial, sans-serif;
  }
  .canvas {
    position: relative;
    width: 1200px;
    height: 1200px;
  }
  .card {
    position: absolute;
    left: 150px;
    width: 900px;
    height: 514px;
    box-shadow: 0 10px 30px rgba(20, 30, 60, 0.18);
    overflow: hidden;
  }

  /* Front: contact side */
  .card-front {
    top: 56px;
    background: var(--white);
  }
  .front-band {
    position: absolute;
    left: 0;
    top: 0;
    width: 300px;
    height: 100%;
    background: var(--navy);
  }
  .front-band-edge {
    position: absolute;
    left: 300px;
    top: 0;
    width: 14px;
    height: 100%;
    background: linear-gradient(180deg, var(--gold-dark), var(--gold-light) 45%, var(--gold) 70%, var(--gold-dark));
  }
  .contact {
    position: absolute;
    right: 60px;
    top: 150px;
    text-align: right;
    color: var(--ink);
  }
  .contact-row {
    display: flex;
    justify-content: flex-end;
    align-items: center;
    gap: 18px;
  }
  .contact-row svg {
    width: 20px;
    height: 20px;
    flex: none;
    fill: var(--navy);
  }
  .person-name {
    font-size: 24px;
    font-weight: 600;
    letter-spacing: 1px;
  }
  .person-role {
    font-size: 11px;
    font-weight: 500;
    letter-spacing: 1.5px;
    margin: 4px 38px 0 0;
  }
  .details {
    margin-top: 48px;
    display: flex;
    flex-direction: column;
    gap: 14px;
    font-size: 17px;
    font-weight: 500;
  }

  /* Back: brand side */
  .card-back {
    top: 630px;
    background: linear-gradient(160deg, var(--navy) 0%, var(--navy-deep) 100%);
  }
  .back-edge {
    position: absolute;
    left: 0;
    top: 0;
    width: 22px;
    height: 100%;
    background: linear-gradient(180deg, var(--gold-dark), var(--gold-light) 40%, var(--gold) 65%, var(--gold-dark));
  }
  .brand {
    position: absolute;
    left: 22px;
    right: 0;
    top: 150px;
    display: flex;
    flex-direction: column;
    align-items: center;
  }
  .brand-mark {
    width: 46px;
    height: 46px;
    background: var(--gold);
    margin-bottom: 22px;
  }
  .brand-name {
    font-size: 68px;
    font-weight: 600;
    letter-spacing: 6px;
    color: var(--white);
    line-height: 1;
  }
  .brand-tagline {
    margin-top: 14px;
    font-size: 20px;
    font-weight: 500;
    letter-spacing: 6px;
    color: var(--gold-light);
  }
</style>
</head>
<body>
<main class="canvas">

  <section class="card card-front" aria-label="Frente do cartão com contatos">
    <div class="front-band"></div>
    <div class="front-band-edge"></div>

    <div class="contact">
      <div class="contact-row">
        <span class="person-name">NOME SOBRENOME</span>
        <svg viewBox="0 0 20 20" aria-hidden="true"><circle cx="10" cy="6" r="4.5"/><path d="M2 19c0-4.5 3.6-7.5 8-7.5s8 3 8 7.5z"/></svg>
      </div>
      <div class="person-role">CARGO / FUNÇÃO</div>

      <div class="details">
        <div class="contact-row">
          <span>nome@empresa.com.br</span>
          <svg viewBox="0 0 20 20" aria-hidden="true"><path d="M1 4h18v12H1z M2.5 5.5 10 11l7.5-5.5" fill="none" stroke="#1b2a52" stroke-width="2"/></svg>
        </div>
        <div class="contact-row">
          <span>99 9999-0000</span>
          <svg viewBox="0 0 20 20" aria-hidden="true"><path d="M3 2h5l1.5 4.5-2.5 1.5a11 11 0 0 0 5 5l1.5-2.5L18 12v5a1.5 1.5 0 0 1-1.5 1.5A15.5 15.5 0 0 1 1.5 3.5 1.5 1.5 0 0 1 3 2z"/></svg>
        </div>
        <div class="contact-row">
          <span>99 99999-9999</span>
          <svg viewBox="0 0 20 20" aria-hidden="true"><rect x="5" y="1" width="10" height="18" rx="2" fill="none" stroke="#1b2a52" stroke-width="2"/><circle cx="10" cy="15.5" r="1.2"/></svg>
        </div>
        <div class="contact-row">
          <span>Rua do Projeto, 999</span>
          <svg viewBox="0 0 20 20" aria-hidden="true"><path d="M10 1a6.5 6.5 0 0 0-6.5 6.5C3.5 12.5 10 19 10 19s6.5-6.5 6.5-11.5A6.5 6.5 0 0 0 10 1zm0 9a2.5 2.5 0 1 1 0-5 2.5 2.5 0 0 1 0 5z"/></svg>
        </div>
      </div>
    </div>
  </section>

  <section class="card card-back" aria-label="Verso do cartão com a marca">
    <div class="back-edge"></div>
    <div class="brand">
      <div class="brand-mark"></div>
      <div class="brand-name">LUMIARA</div>
      <div class="brand-tagline">GESTÃO INTELIGENTE</div>
    </div>
  </section>

</main>
</body>
</html>
```